Business card design and logo for plumbing bussiness

We are wanting a logo for a plumbing business is Queensland Australia. KLV Plumbing and Drainage will be doing works on domestic and commercial sites.
Plumbing, drainage and gas works. We are wanting something that will stand out and be noticed. Colours could be black blue and white but open for suggestions.

Target Market(s)

Builders and home renovators

Industry/Entity Type

Plumbing

Contact Information for Business Card

Dorian Machell - Director
0417 582 031
dorian@klvplumbing-example.com.au
QBCC: 374 8106
ABN: 52 913 207 615

Font styles to use
Sans Serif

Colors
000000

Requirements
Must have
• Clear defined branding

```html
<!DOCTYPE html>
<html lang="en">
<head>
<meta charset="utf-8">
<title>KLV Plumbing – Business Card</title>
<link rel="stylesheet" href="https://fonts.googleapis.com/css2?family=Open+Sans:wght@300;400;600;700&display=swap">
<style>
  :root {
    --stage: #ebebeb;
    --paper: #ffffff;
    --brand-blue: #00aeef;
    --ink: #1a1a1a;
    --ink-soft: #3a3a3a;
  }
  * { margin: 0; padding: 0; box-sizing: border-box; }
  html, body {
    width: 1200px;
    height: 900px;
    overflow: hidden;
    background: var(--stage);
    font-family: "Open Sans", sans-serif;
  }
  .stage {
    position: relative;
    width: 1200px;
    height: 900px;
  }
  .card {
    position: absolute;
    top: 307px;
    width: 500px;
    height: 286px;
    border-radius: 3px;
    box-shadow: 0 10px 28px rgba(0,0,0,0.12);
  }
  .card--front { left: 70px; background: var(--paper); }
  .card--back  { left: 630px; background: var(--brand-blue); }

  .holder {
    position: absolute;
    left: 30px;
    top: 28px;
  }
  .holder__name {
    font-size: 15px;
    font-weight: 700;
    color: var(--brand-blue);
    letter-spacing: 0.02em;
    text-transform: uppercase;
    line-height: 20px;
  }
  .holder__role {
    font-size: 11px;
    color: var(--ink-soft);
    line-height: 15px;
  }

  .contact {
    position: absolute;
    left: 30px;
    top: 94px;
    list-style: none;
    font-size: 11px;
    color: var(--ink-soft);
  }
  .contact__item {
    display: flex;
    align-items: center;
    gap: 7px;
    line-height: 17px;
  }
  .contact__icon { width: 10px; height: 10px; fill: var(--brand-blue); flex: none; }

  .wordmark {
    position: absolute;
    display: flex;
    align-items: center;
    gap: 12px;
    font-weight: 300;
    line-height: 1.2;
    white-space: nowrap;
  }
  .wordmark__dot {
    border-radius: 50%;
    flex: none;
  }
  .card--front .wordmark {
    left: 160px;
    top: 146px;
    font-size: 36px;
    color: var(--ink);
  }
  .card--front .wordmark__dot { width: 18px; height: 18px; background: var(--ink); }
  .card--back .wordmark {
    left: 50%;
    top: 50%;
    transform: translate(-50%, -50%);
    font-size: 38px;
    color: var(--paper);
  }
  .card--back .wordmark__dot { width: 18px; height: 18px; background: var(--paper); }

  .licences {
    position: absolute;
    right: 30px;
    bottom: 24px;
    text-align: right;
    font-size: 11px;
    line-height: 16px;
    color: var(--ink);
  }
  .licences__label { color: var(--brand-blue); }
</style>
</head>
<body>
<main class="stage">
  <section class="card card--front" aria-label="Business card front">
    <div class="holder">
      <p class="holder__name">Dorian Machell</p>
      <p class="holder__role">Director</p>
    </div>

    <ul class="contact">
      <li class="contact__item">
        <svg class="contact__icon" viewBox="0 0 10 10" aria-hidden="true"><path d="M2 0.5 L3.6 2.6 L2.7 3.6 C3.3 5 4.9 6.6 6.4 7.3 L7.4 6.4 L9.5 8 L8.5 9.5 C4.5 9.3 0.7 5.5 0.5 1.5 Z"/></svg>
        <span>0417 582 031</span>
      </li>
      <li class="contact__item">
        <svg class="contact__icon" viewBox="0 0 10 10" aria-hidden="true"><path d="M0.5 2 H9.5 V8.5 H0.5 Z M1 2.4 L5 5.6 L9 2.4" stroke="#fff" stroke-width="0.7"/></svg>
        <span>dorian@klvplumbing-example.com.au</span>
      </li>
    </ul>

    <div class="wordmark">
      <span class="wordmark__dot"></span>
      <span class="wordmark__name">KLV Plumbing</span>
    </div>

    <div class="licences">
      <p><span class="licences__label">QBCC:</span> 374 8106</p>
      <p><span class="licences__label">ABN:</span> 52 913 207 615</p>
    </div>
  </section>

  <section class="card card--back" aria-label="Business card back">
    <div class="wordmark">
      <span class="wordmark__dot"></span>
      <span class="wordmark__name">KLV Plumbing</span>
    </div>
  </section>
</main>
</body>
</html>
```